Business Card Design Project - bel soravin group

dear Sirs

we need business card design for our group ( BEL Soravin Group ) , i have got the Logo design of our group from pixel harbor in previous , so all need details relating to our group i think available with you, as well as the the chosen logo design

we hope to provide us with business card logo that to be appropaite and satisfactory to us .

thanks

note : logo design of our group is attached .
Updates

Reason: please extend the deadline of my project for additional 15 days because i didn't received appropriate design for our gruop yet . kindly beaware that i have received 77 design till now , supossed to send me 200-250 design at least . thanks

Target Market(s)

contents
-

name : Korvan EL Mistrani

position : Operation Manager

Industry/Entity Type

Business

Requirements
Must have

• person name

group logo
Nice to have
• logo color matching with back background

```html
<!DOCTYPE html>
<html lang="en">
<head>
<meta charset="utf-8">
<title>BEL Soravin Group – Business Card</title>
<link rel="stylesheet" href="https://fonts.googleapis.com/css2?family=Nunito+Sans:wght@400;700&display=swap">
<style>
  :root {
    --page-bg: #f1f1f2;
    --front-top: #2c2c2e;
    --front-bottom: #3d3d40;
    --front-mark: #141415;
    --back-light: #5b8dba;
    --back-dark: #2f6196;
    --back-ink: #1d466f;
    --brand-gold: #e6c97e;
    --brand-block: #285887;
    --card-shadow: rgba(0, 0, 0, 0.22);
  }
  * { box-sizing: border-box; margin: 0; padding: 0; }
  html, body {
    width: 1200px;
    height: 1200px;
    overflow: hidden;
    background: var(--page-bg);
    font-family: "Nunito Sans", Verdana, sans-serif;
  }
  .canvas {
    position: relative;
    width: 1200px;
    height: 1200px;
  }
  .card {
    position: absolute;
    left: 150px;
    width: 900px;
    height: 514px;
    overflow: hidden;
    box-shadow: 0 12px 30px var(--card-shadow);
  }
  .card-front {
    top: 64px;
    background: linear-gradient(160deg, var(--front-top), var(--front-bottom));
    display: flex;
    align-items: center;
    justify-content: center;
  }
  .wordmark {
    color: var(--front-mark);
    font-weight: 700;
    line-height: 1;
  }
  .wordmark-name {
    display: block;
    font-size: 64px;
    letter-spacing: 2px;
  }
  .wordmark-tagline {
    display: block;
    margin-top: 8px;
    font-size: 21px;
    letter-spacing: 1px;
  }
  .card-back {
    top: 622px;
    background: linear-gradient(100deg, var(--back-light), var(--back-dark));
    color: var(--back-ink);
    font-weight: 700;
  }
  .holder {
    position: absolute;
    left: 58px;
    top: 92px;
  }
  .holder-name {
    font-size: 36px;
    letter-spacing: 1px;
  }
  .holder-role {
    margin-top: 4px;
    margin-left: 50px;
    font-size: 26px;
    letter-spacing: 1px;
  }
  .contact {
    position: absolute;
    left: 60px;
    top: 290px;
    list-style: none;
    font-size: 25px;
    letter-spacing: 1px;
    line-height: 38px;
  }
  .contact .phone { margin-left: 45px; font-size: 28px; }
  .contact .web,
  .contact .address { margin-left: 45px; }
  .brand-block {
    position: absolute;
    left: 560px;
    top: 70px;
    width: 250px;
    height: 250px;
    background: var(--brand-block);
    opacity: 0.75;
  }
  .brand-name {
    position: absolute;
    left: 520px;
    top: 350px;
    color: var(--brand-gold);
    font-size: 44px;
    font-weight: 700;
    letter-spacing: 2px;
    line-height: 1;
    white-space: nowrap;
  }
</style>
</head>
<body>
  <main class="canvas">
    <section class="card card-front" aria-label="Card front">
      <div class="wordmark">
        <span class="wordmark-name">BEL SORAVIN</span>
        <span class="wordmark-tagline">GROUP OF COMPANIES</span>
      </div>
    </section>

    <section class="card card-back" aria-label="Card back">
      <div class="holder">
        <p class="holder-name">Korvan EL Mistrani</p>
        <p class="holder-role">Operation Manager</p>
      </div>
      <ul class="contact">
        <li class="phone">000 000 0009</li>
        <li class="phone">000 000 0009</li>
        <li class="email">korvanelmistrani@manager.com</li>
        <li class="web">www.belsoravin.com</li>
        <li class="address">Av RL Box 58</li>
      </ul>
      <div class="brand-block" aria-hidden="true"></div>
      <p class="brand-name">BEL SORAVIN</p>
    </section>
  </main>
</body>
</html>
```